Packaging Box for LED Lighted Terrarium Kit

Need to design a packaging box

Target Market(s)

children

Requirements
Must have
• see instruction sheet
Nice to have
• colorful

```html
<!DOCTYPE html>
<html lang="en">
<head>
<meta charset="utf-8">
<title>LED Lighted Terrarium Kit – Box Dieline</title>
<link rel="stylesheet" href="https://fonts.googleapis.com/css2?family=Fredoka:wght@500;600;700&family=Gochi+Hand&family=Nunito:wght@400;700;800&display=swap">
<style>
  :root{
    --stage:#f1f1ef;
    --grass:#6cc62a;
    --sky:#9fe6ea;
    --tangerine:#f26a1b;
    --violet:#4b2aa6;
    --sunny:#ffd21f;
    --alert:#e2262b;
    --ink:#1f1f2b;
    --paper:#ffffff;
    --slate:#1c2a33;
    --brand:#2a3fa0;
    --line:rgba(0,0,0,.18);
  }
  *{box-sizing:border-box;margin:0;padding:0}
  html,body{width:1200px;height:680px;overflow:hidden;background:var(--stage)}
  body{position:relative;font-family:"Nunito",sans-serif;color:var(--ink)}

  .panel{position:absolute;overflow:hidden;border:1px solid var(--line)}
  .panel--top{left:300px;top:80px;width:300px;height:250px;background:var(--grass)}
  .panel--grow{left:50px;top:330px;width:250px;height:250px;background:var(--tangerine)}
  .panel--front{left:300px;top:330px;width:300px;height:250px;background:var(--sky)}
  .panel--glow{left:600px;top:330px;width:250px;height:250px;background:var(--violet)}
  .panel--back{left:850px;top:330px;width:300px;height:250px;background:var(--grass)}

  .hand{font-family:"Gochi Hand",cursive}
  .display{font-family:"Fredoka",sans-serif;font-weight:700;line-height:.95}

  /* maker mark placeholder: plain square + name in one colour/weight */
  .maker-mark{position:absolute;display:flex;align-items:center;gap:5px;background:var(--paper);border-radius:0 0 0 10px;padding:8px 10px;font-family:"Nunito",sans-serif;font-weight:800;font-size:11px;color:var(--brand);white-space:nowrap}
  .maker-mark::before{content:"";width:10px;height:10px;background:var(--alert)}
  .maker-mark--lid{left:60px;top:16px;width:180px;height:46px;justify-content:center;border-radius:8px;font-size:16px}
  .maker-mark--lid::before{width:14px;height:14px}

  .age-tag{position:absolute;background:var(--alert);color:var(--paper);font-family:"Fredoka",sans-serif;font-weight:600;text-align:center;line-height:1;padding:4px 6px;border-radius:3px}
  .age-tag small{display:block;font-size:8px}
  .age-tag b{font-size:15px}

  .fun-strip{position:absolute;background:var(--sunny);color:var(--ink);font-family:"Gochi Hand",cursive;font-size:15px;padding:1px 10px;white-space:nowrap;transform:rotate(-8deg)}
  .brand{position:absolute;font-family:"Nunito",sans-serif;font-weight:800;font-size:8px;color:var(--brand);white-space:nowrap}

  .jar{position:absolute;border-radius:14px 14px 18px 18px}
  .jar--day{background:linear-gradient(180deg,#3d8fe0 0 11%,#e9eef3 11% 58%,#7a5a3a 58% 78%,#d97a2a 78%)}
  .jar--night{background:linear-gradient(180deg,#2e5fd6 0 11%,#7f7de0 11% 58%,#3c3570 58% 80%,#8a4a5a 80%);box-shadow:0 0 14px 4px rgba(160,190,255,.6)}

  .lid-title{position:absolute;left:22px;top:82px;width:256px;text-align:center;color:var(--paper);font-size:30px;transform:rotate(-8deg)}

  .front-title{position:absolute;left:146px;top:70px;color:var(--paper);font-size:23px;white-space:nowrap;transform:rotate(-10deg);text-shadow:2px 2px 0 rgba(0,0,0,.3)}
  .note{position:absolute;color:var(--ink);font-size:13px;line-height:1}

  .tagline{position:absolute;transform:rotate(12deg);white-space:nowrap}
  .tagline__big{font-size:42px;color:var(--sunny)}
  .tagline__small{font-size:22px;color:var(--paper);display:block;margin-top:2px}

  .ask-tag{position:absolute;left:14px;top:30px;background:var(--sunny);font-family:"Gochi Hand",cursive;font-size:16px;padding:1px 8px;white-space:nowrap;transform:rotate(-8deg)}
  .info-card{position:absolute;left:16px;top:58px;width:120px;height:128px;background:var(--paper);padding:7px;font-size:5.6px;line-height:1.35;transform:rotate(-8deg)}
  .info-card p+p{margin-top:4px}
  .kit-card{position:absolute;left:206px;top:18px;width:84px;height:178px;background:var(--slate);border-radius:8px;padding:6px;color:var(--paper)}
  .kit-card h3{font-family:"Gochi Hand",cursive;font-weight:400;font-size:10px;white-space:nowrap;margin-bottom:4px}
  .kit-card ul{list-style:none;background:var(--paper);border-radius:4px;padding:4px;color:var(--ink);font-size:6.5px;line-height:1.7}
  .kit-card li{border-bottom:1px solid #ddd}
  .cta{position:absolute;left:14px;top:196px;width:190px;color:var(--paper);font-weight:800;font-size:9px;line-height:1.2;transform:rotate(-8deg)}
  .legal{position:absolute;right:10px;bottom:6px;font-size:6px;font-weight:700;color:var(--ink)}
</style>
</head>
<body>

<section class="panel panel--top">
  <div class="maker-mark maker-mark--lid">Sprout Lab Kits</div>
  <h1 class="lid-title display">LED Lighted<br>Terrarium Kit</h1>
  <div class="fun-strip" style="left:70px;top:176px">Educational and Fun!</div>
  <div class="brand" style="left:14px;top:222px">Sprout Lab Kits</div>
  <div class="age-tag" style="right:12px;top:12px"><small>Age</small><b>6+</b></div>
</section>

<section class="panel panel--grow">
  <div class="note hand" style="left:8px;top:14px;width:34px;color:var(--sunny)">Wheat and chia plants grow inside!</div>
  <div class="jar jar--day" style="left:42px;top:26px;width:74px;height:170px" role="img" aria-label="Photo of the planted terrarium jar with mushroom house, butterfly and sprouting wheat"></div>
  <div class="maker-mark" style="right:0;top:0">Sprout Lab Kits</div>
  <svg style="position:absolute;left:150px;top:66px" width="64" height="64" viewBox="0 0 64 64" aria-hidden="true">
    <g stroke="#fff" stroke-width="3" stroke-linecap="round">
      <line x1="32" y1="2" x2="32" y2="12"/><line x1="32" y1="52" x2="32" y2="62"/>
      <line x1="2" y1="32" x2="12" y2="32"/><line x1="52" y1="32" x2="62" y2="32"/>
      <line x1="11" y1="11" x2="18" y2="18"/><line x1="46" y1="46" x2="53" y2="53"/>
      <line x1="53" y1="11" x2="46" y2="18"/><line x1="11" y1="53" x2="18" y2="46"/>
    </g>
    <circle cx="32" cy="32" r="14" fill="#fff"/>
  </svg>
  <div class="tagline display" style="left:118px;top:138px"><span class="tagline__big">Grow!</span><span class="tagline__small">under the<br>Sun</span></div>
</section>

<section class="panel panel--front">
  <div class="age-tag" style="left:0;top:14px;border-radius:0 3px 3px 0"><small>Age</small><b>6+</b></div>
  <div class="jar jar--day" style="left:44px;top:54px;width:92px;height:186px" role="img" aria-label="Photo of the terrarium jar with blue LED lid, mushroom house, sunflower and butterfly"></div>
  <div class="note hand" style="left:150px;top:40px;transform:rotate(-10deg)">Is a light!</div>
  <div class="note hand" style="left:6px;top:150px;width:36px">Real plants grow inside!</div>
  <h2 class="front-title display">LED<br>Lighted<br>Terrarium Kit</h2>
  <div class="fun-strip" style="left:158px;top:184px">Educational and Fun!</div>
  <div class="brand" style="left:226px;top:218px">Sprout Lab Kits</div>
  <div class="maker-mark" style="right:0;top:0">Sprout Lab Kits</div>
</section>

<section class="panel panel--glow">
  <div class="jar jar--night" style="left:46px;top:24px;width:80px;height:180px" role="img" aria-label="Photo of the terrarium jar glowing blue in the dark"></div>
  <div class="note hand" style="left:8px;top:80px;width:34px;color:var(--sunny)">LED Light Inside</div>
  <svg style="position:absolute;left:10px;top:10px" width="230" height="90" viewBox="0 0 230 90" aria-hidden="true">
    <g stroke="#ffd21f" stroke-width="3" stroke-linecap="round">
      <line x1="6" y1="10" x2="32" y2="26"/><line x1="4" y1="34" x2="32" y2="40"/><line x1="8" y1="58" x2="32" y2="54"/>
      <line x1="132" y1="44" x2="162" y2="36"/><line x1="134" y1="58" x2="168" y2="58"/><line x1="132" y1="72" x2="162" y2="80"/>
    </g>
  </svg>
  <svg style="position:absolute;left:176px;top:80px" width="44" height="50" viewBox="0 0 44 50" aria-hidden="true">
    <path d="M26 2 A24 24 0 1 0 42 40 A18 18 0 1 1 26 2 Z" fill="#fff"/>
  </svg>
  <div class="tagline display" style="left:118px;top:138px"><span class="tagline__big">Glow!</span><span class="tagline__small">under the<br>Moon</span></div>
  <div class="maker-mark" style="right:0;top:0">Sprout Lab Kits</div>
</section>

<section class="panel panel--back">
  <div class="ask-tag">What is a terrarium?</div>
  <div class="info-card">
    <p><b>A terrarium is a miniature, tabletop garden in a container that mimics the natural world outside.</b> It's a piece of nature that is small enough to hold in your hands.</p>
    <p>Terrariums can be in any glass container, like a fish bowl or even an old, empty light bulb. <b>Sprout Lab Kits Light-up Terrarium is the ideal size for you to observe a mini ecosystem up close right on your desk.</b></p>
    <p>As soon as you plant your terrarium, you'll find out not just what it takes for plants to grow, but also how fun and exciting gardening can be!</p>
  </div>
  <div class="jar jar--day" style="left:146px;top:70px;width:54px;height:112px" role="img" aria-label="Small photo of the finished terrarium jar"></div>
  <div class="kit-card">
    <h3>What's in your kit?</h3>
    <ul>
      <li>Jar</li><li>LED lid</li><li>USB cable</li><li>Soil</li><li>Orange sand</li>
      <li>Chia seeds</li><li>Wheat seeds</li><li>White stones</li><li>Spray bottle</li><li>Stickers</li>
    </ul>
  </div>
  <p class="cta">Are you ready to dive in, put together your terrarium today, and start weeks of fascinating, scientific fun?</p>
  <p class="legal">Made in China / www.sproutlabkits.com</p>
</section>

</body>
</html>
```